Business card design needed

New company in Executive Search & Consulting (Recruitment & Head Hunting Company)

We recruit IT, Accounting & Finance, Human Resources and Senior Management

with offices in Harrow, Eastmere, Lindel and Port Aven

Industry/Entity Type

Business

Contact Information for Business Card

Calderwood-Ashfield Executive Search & Consulting
*Harrow *Eastmere * Lindel * Port Aven
Neil Calderwood Australian Director
147 Mellor Street Subiaco Western Australia
www.calderwoodashfield.example.au
Ph: 08 6000 4827 Fax: 08 6000 9153
Mobile: 0400 731 562

```html
<!DOCTYPE html>
<html lang="en">
<head>
<meta charset="utf-8">
<title>Calderwood-Ashfield Business Card</title>
<link rel="stylesheet" href="https://fonts.googleapis.com/css2?family=Cinzel:wght@400;500&display=swap">
<style>
  :root {
    --page-bg: #e9e7e4;
    --card-bg: #ffffff;
    --ink: #3a4e5c;
    --ink-soft: #4d6070;
    --band-light: #c6d2d8;
    --band-text: #ffffff;
    --art-light: #f6f8f9;
    --art-mid: #b4bfc7;
  }
  * { margin: 0; padding: 0; box-sizing: border-box; }
  html, body { width: 1200px; height: 1000px; overflow: hidden; }
  body {
    position: relative;
    background: var(--page-bg);
    font-family: "Cinzel", Georgia, serif;
    color: var(--ink);
  }
  .card {
    position: absolute;
    width: 580px;
    height: 354px;
    background: var(--card-bg);
    border-radius: 14px;
    overflow: hidden;
    box-shadow: 0 6px 14px rgba(0,0,0,0.22);
  }
  .card--front { left: 242px; top: 128px; }
  .card--back  { left: 352px; top: 500px; }

  .front-art {
    position: absolute;
    left: 0; top: 0;
    width: 290px; height: 225px;
    background: radial-gradient(ellipse 70% 75% at 35% 45%, var(--art-light) 0%, var(--art-mid) 60%, rgba(255,255,255,0) 100%);
  }
  .holder { position: absolute; right: 42px; text-align: right; white-space: nowrap; }
  .holder__name { top: 104px; font-size: 23px; font-weight: 500; letter-spacing: 1px; }
  .holder__title { top: 134px; font-size: 10.5px; font-weight: 500; letter-spacing: 0.3px; }
  .contact {
    position: absolute;
    right: 36px; top: 204px;
    text-align: right;
    font-size: 13.5px;
    line-height: 17px;
    color: var(--ink-soft);
    white-space: nowrap;
  }
  .front-band {
    position: absolute;
    left: 0; bottom: 0;
    width: 100%; height: 29px;
    background: var(--band-light);
    text-align: center;
    font-size: 12.5px;
    line-height: 29px;
    font-weight: 400;
    color: var(--ink);
    letter-spacing: 0.3px;
  }

  .brand {
    position: absolute;
    left: 0; width: 100%;
    text-align: center;
    white-space: nowrap;
  }
  .brand__name { top: 182px; font-size: 29px; letter-spacing: 1px; color: var(--ink); }
  .brand__mark {
    display: inline-block;
    width: 14px; height: 14px;
    margin-right: 12px;
    background: var(--ink-soft);
    vertical-align: 3px;
  }
  .brand__tagline { top: 222px; font-size: 15px; letter-spacing: 1px; color: var(--ink-soft); }

  .back-band {
    position: absolute;
    left: 0; bottom: 0;
    width: 100%; height: 44px;
  }
  .offices {
    position: absolute;
    left: 0; bottom: 0;
    width: 100%; height: 32px;
    text-align: center;
    font-size: 16.5px;
    line-height: 30px;
    color: var(--band-text);
    letter-spacing: 1px;
    white-space: nowrap;
  }
  .offices .sep { margin: 0 16px; }
</style>
</head>
<body>
  <section class="card card--front">
    <div class="front-art" role="img" aria-label="Large metallic 3D puzzle piece illustration"></div>
    <div class="holder holder__name">Neil Calderwood</div>
    <div class="holder holder__title">Australian Director</div>
    <div class="contact">
      147 Mellor Street<br>
      Kellmore Western Region<br>
      P: 08 6000 4827<br>
      F: 08 6000 9153<br>
      M: 0400 731 562
    </div>
    <div class="front-band">www.calderwoodashfield.example.au</div>
  </section>

  <section class="card card--back">
    <div class="brand brand__name"><span class="brand__mark"></span>Calderwood Ashfield</div>
    <div class="brand brand__tagline">Executive Search &amp; Consulting</div>
    <svg class="back-band" width="580" height="44" viewBox="0 0 580 44" aria-hidden="true">
      <defs>
        <linearGradient id="bandFill" x1="0" y1="0" x2="0" y2="1">
          <stop offset="0" stop-color="#7a8d9a"/>
          <stop offset="1" stop-color="#566b79"/>
        </linearGradient>
      </defs>
      <polygon points="282,8 290,0 298,8" fill="#566b79"/>
      <rect x="0" y="8" width="580" height="2" fill="#566b79"/>
      <rect x="0" y="12" width="580" height="32" fill="url(#bandFill)"/>
    </svg>
    <div class="offices">Harrow<span class="sep">|</span>Eastmere<span class="sep">|</span>Lindel<span class="sep">|</span>Port Aven</div>
  </section>
</body>
</html>
```